Business card for Luxury Portable Restroom Trailer company

We are a Luxury Portable Restroom Trailer Company Called FALVEX HIRINGS. Based in Orange County California. We provide portable restroom trailers for events, such as, Weddings, Concerts, Charity events, Sporting events, Tournaments, Corporate events, ect. We rent and Sell the Luxury restrooms. Our colors are white, grey, and Orange. As you will see in the logo we uploaded.
There are 2 people in the company so the names and titles will change for the 3 people but card will remain the same. Here is the information for each Person: Desmond Purt CFO 555 018-3374
next Person: Milo Fenwright VP 555 018-3374
Next Person: Owen Fenwright CEO 555 018-3374
Information to include on the card: Luxury Restroom Trailers Rental and Sales. Weddings, Concerts, Charity, Sporting and Corp. Events.

```html
<!DOCTYPE html>
<html lang="en">
<head>
<meta charset="utf-8">
<title>Falvex Hirings – Business Card</title>
<link href="https://fonts.googleapis.com/css2?family=Open+Sans:wght@400;600;700;800&display=swap" rel="stylesheet">
<style>
  :root{
    --stage:#232323;
    --paper:#fffdf3;
    --peach:#fbe6d4;
    --orange:#f0621f;
    --grey:#4a4a4c;
    --ink:#2e2e30;
  }
  *{box-sizing:border-box;margin:0;padding:0}
  html,body{width:1200px;height:768px;overflow:hidden;background:var(--stage)}
  body{font-family:"Open Sans",Arial,sans-serif;position:relative}
  .card{
    position:absolute;top:230px;width:530px;height:303px;
    background:var(--paper);overflow:hidden;
  }
  .card--back{left:40px}
  .card--front{left:630px}
  .card__motif{
    position:absolute;
    background:radial-gradient(ellipse at 55% 50%,var(--peach) 0%,var(--peach) 45%,rgba(251,230,212,0) 72%);
  }
  .card--back .card__motif{left:170px;top:-30px;width:360px;height:300px}
  .card--front .card__motif{left:40px;top:-40px;width:470px;height:380px}
  .brand{
    display:flex;align-items:center;gap:10px;
    color:var(--orange);font-weight:800;letter-spacing:1px;position:absolute;
  }
  .brand__mark{width:12px;height:12px;background:var(--orange)}
  .card--back .brand{left:26px;top:26px;font-size:24px}
  .card--front .brand{left:50%;top:50%;transform:translate(-50%,-50%);font-size:36px;white-space:nowrap}
  .card--front .brand__mark{width:18px;height:18px}
  .accent{position:absolute;right:0;top:100px;width:14px;height:44px;background:var(--orange)}
  .person{position:absolute;right:30px;top:96px;text-align:right}
  .person__name{font-size:26px;font-weight:600;line-height:1.1}
  .person__first{color:var(--orange)}
  .person__last{color:var(--grey)}
  .person__title{font-size:12px;color:var(--ink);margin-top:1px}
  .contacts,.services{
    position:absolute;right:30px;list-style:none;text-align:right;
    font-size:12px;line-height:15px;color:var(--ink);white-space:nowrap
  }
  .contacts{top:146px}
  .services{top:206px}
  .contacts li,.services li{display:flex;align-items:center;justify-content:flex-end;gap:6px}
  .icon{width:10px;height:10px;fill:var(--orange);flex:none}
  .tagline{position:absolute;left:26px;bottom:18px;font-size:13px;color:var(--ink);white-space:nowrap}
</style>
</head>
<body>
  <section class="card card--back" aria-label="Business card, back">
    <div class="card__motif" role="img" aria-label="Faint large brand animal silhouette in soft peach"></div>
    <div class="brand"><span class="brand__mark"></span>FALVEX HIRINGS</div>
    <div class="accent"></div>
    <div class="person">
      <div class="person__name"><span class="person__first">Desmond</span> <span class="person__last">Purt</span></div>
      <div class="person__title">CFO</div>
    </div>
    <ul class="contacts">
      <li>555 018-3374
        <svg class="icon" viewBox="0 0 10 10"><path d="M2 0.5 L4 2.5 L3 4 Q4 6 6 7 L7.5 6 L9.5 8 L8 9.5 Q1 8.5 0.5 2Z"/></svg></li>
      <li>info@falvexhirings.com
        <svg class="icon" viewBox="0 0 10 10"><path d="M0 2h10v6H0z M0 2l5 3.5L10 2" fill="none" stroke="var(--orange)" stroke-width="1.4"/></svg></li>
      <li>www.falvexhirings.com
        <svg class="icon" viewBox="0 0 10 10"><circle cx="5" cy="5" r="4.2" fill="none" stroke="var(--orange)" stroke-width="1.4"/><path d="M1 5h8M5 1v8" stroke="var(--orange)" stroke-width="1"/></svg></li>
    </ul>
    <ul class="services">
      <li>Events <svg class="icon" viewBox="0 0 10 10"><rect x="1" y="1" width="8" height="8" rx="1.5"/></svg></li>
      <li>Charity <svg class="icon" viewBox="0 0 10 10"><rect x="1" y="1" width="8" height="8" rx="1.5"/></svg></li>
      <li>Concerts <svg class="icon" viewBox="0 0 10 10"><rect x="1" y="1" width="8" height="8" rx="1.5"/></svg></li>
      <li>Weddings <svg class="icon" viewBox="0 0 10 10"><rect x="1" y="1" width="8" height="8" rx="1.5"/></svg></li>
      <li>Sporting and Corp <svg class="icon" viewBox="0 0 10 10"><rect x="1" y="1" width="8" height="8" rx="1.5"/></svg></li>
    </ul>
    <p class="tagline">Luxury Restroom Trailers Rental and Sales</p>
  </section>

  <section class="card card--front" aria-label="Business card, front">
    <div class="card__motif" role="img" aria-label="Faint large brand animal silhouette in soft peach"></div>
    <div class="brand"><span class="brand__mark"></span>FALVEX HIRINGS</div>
  </section>
</body>
</html>
```